Property Development Business Cards

I need a business card design for Blue Harbour Developments Pty Ltd. We are a property development company in Australia and our name defines the five values that we adhere to, being Profitable, Partnerships, Quality Developments, Eco Friendly and Enduring Design.

I have attached the current logo that I use, it is just five yellow circles connected to a single cricle in the middle.

Target Market(s)

Our Target audience is real estate agents, owners of properties, builders and other trades

Industry/Entity Type

Business

Requirements
Must have
• Want to have two sides to the card, one with details and one to just highlight the company

```html
<!DOCTYPE html>
<html lang="en">
<head>
<meta charset="utf-8">
<title>Blue Harbour Developments Pty Ltd — Business Cards</title>
<link rel="stylesheet" href="https://fonts.googleapis.com/css2?family=Roboto+Condensed:wght@700&display=swap">
<style>
  :root {
    --yellow: #ffd23f;
    --navy: #3f4575;
    --ink: #2c3142;
    --value-grey: #8c8c8c;
    --card-edge: #cfcfcf;
    --paper: #ffffff;
    --pattern-tone: #e9e9ec;
  }
  * { margin: 0; padding: 0; box-sizing: border-box; }
  html, body {
    width: 1200px; height: 1008px; overflow: hidden;
    background: var(--paper);
    font-family: "Roboto Condensed", "Arial Narrow", sans-serif;
    font-weight: 700;
  }
  .card {
    position: absolute; top: 0;
    width: 575px; height: 1006px;
    border: 1px solid var(--card-edge);
    background: var(--paper);
    overflow: hidden;
  }
  .card--front { left: 0; }
  .card--back { left: 625px; }

  .band { position: absolute; left: 0; right: 0; }
  .band--top-yellow { top: 0; height: 19px; background: var(--yellow); }
  .band--top-navy { top: 25px; height: 8px; background: var(--navy); }
  .band--bottom-navy { top: 886px; height: 13px; background: var(--navy); }
  .band--bottom-yellow { top: 912px; height: 35px; background: var(--yellow); }

  .arc-pattern {
    position: absolute; left: 0; top: 340px;
    width: 575px; height: 546px;
    background: radial-gradient(ellipse at 100% 100%, rgba(255,255,255,0) 30%, var(--pattern-tone) 60%, rgba(255,255,255,0) 85%);
    opacity: .7;
  }

  .brand-dot {
    position: absolute; border-radius: 50%;
    background: radial-gradient(circle at 35% 35%, #fff3a8, var(--yellow) 55%, #f2b600);
  }
  .card--front .brand-dot { left: 92px; top: 150px; width: 52px; height: 52px; }
  .card--back .brand-dot { left: 84px; top: 105px; width: 30px; height: 30px; }

  .company-name { position: absolute; color: var(--ink); white-space: nowrap; letter-spacing: -.2px; }
  .card--front .company-name { left: 52px; top: 268px; font-size: 31px; }
  .card--back .company-name { left: 48px; top: 180px; font-size: 23px; }

  .values { position: absolute; right: 86px; top: 244px; list-style: none; }
  .values li {
    display: flex; align-items: center; justify-content: flex-end;
    height: 48.5px; font-size: 29px; color: var(--value-grey);
  }
  .values svg { margin-left: 22px; width: 14px; height: 14px; }
</style>
</head>
<body>
  <section class="card card--front">
    <div class="band band--top-yellow"></div>
    <div class="band band--top-navy"></div>
    <div class="arc-pattern" role="img" aria-label="Decorative sweep of fine curved lines"></div>
    <div class="brand-dot"></div>
    <h1 class="company-name">Blue Harbour Developments Pty Ltd</h1>
    <div class="band band--bottom-navy"></div>
    <div class="band band--bottom-yellow"></div>
  </section>

  <section class="card card--back">
    <div class="band band--top-yellow"></div>
    <div class="band band--top-navy"></div>
    <div class="arc-pattern" role="img" aria-label="Decorative sweep of fine curved lines"></div>
    <div class="brand-dot"></div>
    <h2 class="company-name">Blue Harbour Developments Pty Ltd</h2>
    <ul class="values">
      <li>Profitable<svg viewBox="0 0 14 14"><path d="M2 2 L12 7 L2 12 L5 7 Z" fill="var(--yellow)" stroke="#d9a800" stroke-width="1"/></svg></li>
      <li>Partnerships<svg viewBox="0 0 14 14"><path d="M2 2 L12 7 L2 12 L5 7 Z" fill="var(--yellow)" stroke="#d9a800" stroke-width="1"/></svg></li>
      <li>Quality Developments<svg viewBox="0 0 14 14"><path d="M2 2 L12 7 L2 12 L5 7 Z" fill="var(--yellow)" stroke="#d9a800" stroke-width="1"/></svg></li>
      <li>Eco Friendly<svg viewBox="0 0 14 14"><path d="M2 2 L12 7 L2 12 L5 7 Z" fill="var(--yellow)" stroke="#d9a800" stroke-width="1"/></svg></li>
      <li>Enduring Design<svg viewBox="0 0 14 14"><path d="M2 2 L12 7 L2 12 L5 7 Z" fill="var(--yellow)" stroke="#d9a800" stroke-width="1"/></svg></li>
    </ul>
    <div class="band band--bottom-navy"></div>
    <div class="band band--bottom-yellow"></div>
  </section>
</body>
</html>
```